Visitenkarten für Erstellung von Beleihungswert- und Verkehrswertgutachten.
Zielgruppe
Ich erstelle Beleihungswert- und Verkehrswertgutachten.
Meine Zielgruppe sind alle Immobilieneigentümer, Kaufinteressenten, Erben von Immobilienvermögen evtl. auch Anwälte, Steuerberater.
Aufgabenstellung
Der Fokus liegt auf der Wertermittlung von Immobilien

```html
<!DOCTYPE html>
<html lang="de">
<head>
<meta charset="utf-8">
<title>Velden Immobilien Bewertung – Visitenkarten</title>
<link href="https://fonts.googleapis.com/css2?family=Catamaran:wght@400;500;600;700&display=swap" rel="stylesheet">
<style>
  :root {
    --page: #f5f5f5;
    --ink: #555555;
    --ink-dark: #1c1c1c;
    --gold: #b48a32;
    --gold-light: #c9a95a;
    --gray-card: #707070;
    --navy: #0b2a3d;
    --white: #ffffff;
  }
  * { margin: 0; padding: 0; box-sizing: border-box; }
  html, body { width: 814px; height: 1200px; overflow: hidden; background: var(--page); }
  body { position: relative; font-family: "Catamaran", sans-serif; color: var(--ink); }

  .brand {
    position: absolute; left: 0; top: 120px; width: 814px;
    display: flex; justify-content: center; align-items: center; gap: 10px;
  }
  .brand-square { width: 14px; height: 14px; background: var(--gold); }
  .brand-name { font-size: 25px; font-weight: 700; letter-spacing: 1.2px; color: var(--ink); }

  .card {
    position: absolute; top: 264px; width: 358px; height: 232px; overflow: hidden;
    box-shadow: 6px 10px 14px rgba(0,0,0,0.22);
  }
  .card svg.card-bg { position: absolute; inset: 0; }
  .card-front { left: 36px; background: var(--white); }
  .card-back { left: 418px; background: var(--gray-card); }

  .card-brand {
    position: absolute; left: 0; width: 100%; text-align: center;
    font-weight: 700; letter-spacing: 0.8px;
  }
  .card-front .card-brand { top: 84px; font-size: 15px; color: var(--ink); }
  .card-back .card-brand { top: 106px; font-size: 15px; color: var(--gold-light); }

  .holder {
    position: absolute; top: 120px; width: 100%; text-align: center;
    font-size: 13px; font-weight: 700; color: var(--ink-dark);
  }
  .contact {
    position: absolute; top: 143px; left: 118px;
    font-size: 11px; font-weight: 500; color: var(--ink-dark); line-height: 13px;
  }
  .contact li { list-style: none; display: flex; align-items: center; gap: 6px; }
  .contact svg { width: 12px; height: 11px; }

  .address {
    position: absolute; top: 193px; font-size: 10px; font-weight: 600;
    color: var(--white); line-height: 12.5px; letter-spacing: 0.3px;
  }
  .address-left { left: 15px; }
  .address-right { right: 16px; text-align: right; }

  .qualifications {
    position: absolute; top: 165px; width: 100%; text-align: center;
    font-size: 8.6px; color: var(--white); line-height: 13.3px; letter-spacing: 0.15px;
  }
  .qualifications b { font-weight: 600; }
</style>
</head>
<body>

  <header class="brand">
    <span class="brand-square"></span>
    <span class="brand-name">Velden Immobilien Bewertung</span>
  </header>

  <section class="card card-front" aria-label="Visitenkarte Vorderseite">
    <svg class="card-bg" viewBox="0 0 358 232" width="358" height="232">
      <defs>
        <linearGradient id="goldFront" x1="0" x2="1" y1="0" y2="0">
          <stop offset="0" stop-color="#a97b1f"/>
          <stop offset="0.5" stop-color="#c9a955"/>
          <stop offset="1" stop-color="#a97b1f"/>
        </linearGradient>
      </defs>
      <path d="M0,134 Q179,254 358,134 L358,232 L0,232 Z" fill="url(#goldFront)"/>
      <path d="M0,128 Q179,248 358,128" fill="none" stroke="var(--navy)" stroke-width="3"/>
    </svg>
    <div class="card-brand">Velden Immobilien Bewertung</div>
    <div class="holder">Marlene Velden</div>
    <ul class="contact">
      <li>
        <svg viewBox="0 0 12 11"><rect x="1" y="1" width="5" height="9" rx="1" fill="none" stroke="var(--gold)" stroke-width="1.2"/><circle cx="9" cy="2.5" r="2.3" fill="var(--gold)"/></svg>
        +49 170 - 5550123
      </li>
      <li>
        <svg viewBox="0 0 12 11"><rect x="0.5" y="2" width="11" height="7" fill="var(--gold)"/><path d="M0.5,2 L6,6 L11.5,2" fill="none" stroke="var(--white)" stroke-width="0.8"/></svg>
        m. velden@example.de
      </li>
    </ul>
    <address class="address address-left" style="font-style:normal">Lindenhofweg 4/2<br>70000 Musterstadt</address>
    <address class="address address-right" style="font-style:normal">Werkstraße 18<br>77000 Beispielheim</address>
  </section>

  <section class="card card-back" aria-label="Visitenkarte Rückseite">
    <svg class="card-bg" viewBox="0 0 358 232" width="358" height="232">
      <defs>
        <linearGradient id="goldBack" x1="0" x2="1" y1="0" y2="0">
          <stop offset="0" stop-color="#a97b1f"/>
          <stop offset="0.5" stop-color="#c9a955"/>
          <stop offset="1" stop-color="#a97b1f"/>
        </linearGradient>
      </defs>
      <path d="M0,104 Q179,222 358,104 L358,232 L0,232 Z" fill="url(#goldBack)"/>
      <path d="M0,99 Q179,217 358,99" fill="none" stroke="#1a1a1a" stroke-width="4"/>
    </svg>
    <div class="card-brand">Velden Immobilien Bewertung</div>
    <p class="qualifications">
      <b>DIN ISO/IEC 17024</b> zertifizierte Bau-Sachverständige für die Markt-<br>
      und Beleihungswertermittlung von Wohn- und Gewerbeimmobilie<br>
      <b>VERTA D1, D2 und D3 zertifiziert</b><br>
      <b>SIGEKO</b> = Sicherheits- und Gesundheitsschutz-Koordinator für Baustellen.
    </p>
  </section>

</body>
</html>
```